Carpet cleaning company focused on high quality needs business cards

We are a growing company that just merged with another company and need to design a new business card. We do both residential as well as commercial cleaning. We do carpet, tile & grout, upholstery, hard floors, and stain & pet odor removal. We treat our customers like family and strive to achieve outstanding results with every job.

```html
<!DOCTYPE html>
<html lang="en">
<head>
<meta charset="UTF-8">
<title>Fairfield Steam Crew – Business Cards</title>
<link href="https://fonts.googleapis.com/css2?family=Lato:wght@400;700;900&display=swap" rel="stylesheet">
<style>
  :root{
    --bg:#2b2b2d;
    --card:#ffffff;
    --card-shade:#ececec;
    --ink:#3a3a3a;
    --black:#111111;
    --blue:#1a7fc6;
    --red:#e0413a;
    --pink:#f7dcdc;
  }
  *{box-sizing:border-box;margin:0;padding:0}
  html,body{width:1200px;height:900px;overflow:hidden}
  body{background:var(--bg);font-family:"Lato",sans-serif;color:var(--ink);position:relative}

  .card{position:absolute;width:620px;height:354px;
    background:linear-gradient(135deg,var(--card) 0%,var(--card) 55%,var(--card-shade) 100%);
    box-shadow:0 10px 30px rgba(0,0,0,.5);overflow:hidden}
  .card--services{left:50px;top:50px}
  .card--contact{left:530px;top:496px}

  .brand{position:absolute;display:flex;align-items:center;gap:14px}
  .brand__mark{width:64px;height:64px;background:var(--red)}
  .brand__name{font-weight:900;font-size:26px;line-height:1;color:var(--black);text-transform:uppercase;width:170px}

  .card--services .brand{left:36px;top:110px}

  .services{position:absolute;right:34px;top:28px;text-align:right}
  .heading{color:var(--blue);font-weight:700;font-size:17px;text-transform:uppercase;letter-spacing:.3px}
  .services__list{list-style:none;margin-top:8px}
  .services__list li{font-size:14px;line-height:22px;display:flex;justify-content:flex-end;align-items:center;gap:8px}
  .services__list svg{width:12px;height:12px}

  .hours{position:absolute;left:36px;bottom:34px}
  .hours__row{font-size:14px;line-height:20px;margin-top:4px}
  .hours__days{color:var(--blue)}

  .tagline{position:absolute;right:0;bottom:40px;width:290px;height:34px;background:var(--blue);
    color:#fff;font-weight:700;font-size:14px;display:flex;align-items:center;padding-left:18px}

  .card--contact .brand{right:40px;top:30px}
  .divider{position:absolute;left:80px;right:30px;top:124px;height:1px;background:var(--red)}
  .decor{position:absolute;left:0;bottom:0;width:300px;height:220px;
    background:linear-gradient(180deg,rgba(247,220,220,.15),var(--pink))}
  .areas{position:absolute;right:36px;top:150px;text-align:right;font-size:13.5px;line-height:20px}

  .person{position:absolute;left:40px;bottom:104px}
  .person__name{color:var(--blue);font-weight:700;font-size:19px;text-transform:uppercase}
  .person__role{font-size:14px;margin-top:2px}
  .contacts{position:absolute;left:40px;bottom:24px;list-style:none}
  .contacts li{display:flex;align-items:center;gap:10px;font-size:14px;line-height:24px}
  .contacts svg{width:14px;height:14px;fill:none;stroke:var(--blue);stroke-width:2}
</style>
</head>
<body>

<section class="card card--services">
  <div class="brand">
    <span class="brand__mark"></span>
    <span class="brand__name">Fairfield Steam Crew</span>
  </div>

  <div class="services">
    <h2 class="heading">Our Services</h2>
    <ul class="services__list">
      <li>Natural Carpets<svg viewBox="0 0 12 12"><circle cx="6" cy="6" r="4.5" fill="none" stroke="#1a7fc6" stroke-width="1.5"/></svg></li>
      <li>Residential Carpet Cleaning<svg viewBox="0 0 12 12"><circle cx="6" cy="6" r="4.5" fill="none" stroke="#1a7fc6" stroke-width="1.5"/></svg></li>
      <li>Tile &amp; Grout<svg viewBox="0 0 12 12"><circle cx="6" cy="6" r="4.5" fill="none" stroke="#1a7fc6" stroke-width="1.5"/></svg></li>
      <li>Upholstery<svg viewBox="0 0 12 12"><circle cx="6" cy="6" r="4.5" fill="none" stroke="#1a7fc6" stroke-width="1.5"/></svg></li>
      <li>Hard Floors<svg viewBox="0 0 12 12"><circle cx="6" cy="6" r="4.5" fill="none" stroke="#1a7fc6" stroke-width="1.5"/></svg></li>
      <li>Dining Room And Office Chairs<svg viewBox="0 0 12 12"><circle cx="6" cy="6" r="4.5" fill="none" stroke="#1a7fc6" stroke-width="1.5"/></svg></li>
      <li>Stain &amp; Pet Odor Removal<svg viewBox="0 0 12 12"><circle cx="6" cy="6" r="4.5" fill="none" stroke="#1a7fc6" stroke-width="1.5"/></svg></li>
    </ul>
  </div>

  <div class="hours">
    <h2 class="heading">Our Services Time</h2>
    <p class="hours__row"><span class="hours__days">Mon.Tue.Wed.Thur.Fri-</span> 9:00am - 6:00pm</p>
    <p class="hours__row"><span class="hours__days">Sat.Sun-</span> Closed</p>
  </div>

  <div class="tagline">A Clean Like You've Never Seen</div>
</section>

<section class="card card--contact">
  <div class="decor" role="img" aria-label="Faint backdrop block behind the contact details"></div>
  <div class="brand">
    <span class="brand__mark"></span>
    <span class="brand__name">Fairfield Steam Crew</span>
  </div>
  <div class="divider"></div>

  <address class="areas" style="font-style:normal">
    Gahanna, OH, US<br>
    Reynoldsburg, OH, US<br>
    Pickerington, OH, US<br>
    New Albany, OH, US<br>
    Columbus, OH, US
  </address>

  <div class="person">
    <h2 class="person__name">Fairfield Steam Crew</h2>
    <p class="person__role">Owner</p>
  </div>

  <ul class="contacts">
    <li><svg viewBox="0 0 16 16"><path d="M3 2l3 1 1 3-2 1.5a8 8 0 0 0 3.5 3.5L10 9l3 1 1 3-2 1.5C7 14 2 9 1.5 4z"/></svg>(614) 555-0182</li>
    <li><svg viewBox="0 0 16 16"><rect x="1.5" y="3.5" width="13" height="9"/><path d="M1.5 3.5L8 9l6.5-5.5"/></svg>hello@fairfieldsteamcrew.com</li>
    <li><svg viewBox="0 0 16 16"><circle cx="8" cy="8" r="6.5"/><path d="M1.5 8h13M8 1.5c3 3.5 3 9.5 0 13M8 1.5c-3 3.5-3 9.5 0 13"/></svg>www.fairfieldsteamcrew.com</li>
  </ul>
</section>

</body>
</html>
```